Looking for a tri-fold flyer for a new energy conservation company

We are a locally owned energy conservation company that focuses on making energy efficiency upgrades to residential, commercial, and agricultural properties. Services range from solar, re-roofs, dual pane windows, HVAC's, tankless water heaters, water efficient products, I have a list of items I can upload to show all services and pictures of a website that we are building currently. I would like the tri fold to include who, what, why info I have attached. I would like to see a modern design with Bold Capitalized text, our blue color to be used a lot with the green maybe accent colors.

Target Market(s)

please see attachment

Industry/Entity Type

It Company

Requirements
Must have
• please see attachment
Nice to have
• please see attachment
Should not have
• Colors requested below are in the logo that is attached as a PSD file.

```html
<!DOCTYPE html>
<html lang="en">
<head>
<meta charset="utf-8">
<title>BrightLeaf Energy – Tri-fold Brochure</title>
<link href="https://fonts.googleapis.com/css2?family=Open+Sans:wght@400;600;700;800&display=swap" rel="stylesheet">
<style>
:root{
  --blue:#1a9ad6;
  --blue-dark:#137fb3;
  --green:#8dc63f;
  --green-dark:#6fa92b;
  --ink:#4a4a4a;
  --paper:#ffffff;
  --backdrop:#a7a9ac;
}
*{box-sizing:border-box;margin:0;padding:0}
html,body{width:1200px;height:3863px;overflow:hidden}
body{background:var(--backdrop);font-family:"Open Sans",Arial,sans-serif;color:var(--ink);position:relative}

.cover-view{position:absolute;left:300px;top:271px;width:375px;height:772px;transform:scale(1.6);transform-origin:top left}
.spread{position:absolute;left:37px;width:1125px;height:772px;background:var(--paper);display:flex;box-shadow:0 4px 14px rgba(0,0,0,.25);overflow:hidden}
.spread.outside{top:1777px}
.spread.inside{top:2820px}
.panel{position:relative;width:375px;height:772px;padding:34px 30px 0}
.cover-view .panel{background:var(--paper);box-shadow:0 4px 14px rgba(0,0,0,.25)}

h2{color:var(--blue);font-weight:700;font-size:19px;text-transform:uppercase;text-align:center;letter-spacing:.5px;margin-bottom:14px}
p{font-size:11.2px;line-height:1.55}
.section+.section{margin-top:34px}

.photo{position:absolute}
.brand{display:flex;align-items:center;gap:8px;color:var(--blue);font-weight:700;font-size:25px;line-height:1}
.brand .dot{width:26px;height:26px;border-radius:50%;background:var(--green);flex:none}

/* outside left */
.team-photo{left:0;bottom:0;width:340px;height:205px;border-top-right-radius:150px 110px;border-top:5px solid var(--blue);border-right:5px solid var(--blue);background:linear-gradient(135deg,#c9a88f,#7a5b4a 55%,#d8d0c4)}

/* outside middle */
.mid-brand{justify-content:center;margin:40px 0 30px}
.contact{text-align:center;font-size:11.2px;line-height:1.5}
.contact .icon{display:block;margin:0 auto 8px}
.contact .group{margin-bottom:16px}

/* cover */
.cover .brand{margin:8px 0 0 22px}
.nature-band{position:absolute;left:30px;right:0;top:84px;height:82px;background:var(--green);color:#fff;padding:10px 0 0 40px;text-transform:uppercase}
.nature-band .small{font-size:18px;font-weight:600;display:block;line-height:1.1}
.nature-band .big{font-size:36px;font-weight:800;display:block;line-height:1.15;letter-spacing:1px}
.man-photo{left:60px;top:200px;width:270px;height:330px;background:linear-gradient(180deg,#e9eef1,#cfd8de 40%,#2b3440 70%,#1d232b)}
.web-bar{position:absolute;right:0;top:622px;width:330px;height:48px;background:var(--blue);border-radius:16px 0 0 0;color:#fff;font-weight:700;font-size:14px;display:flex;align-items:center;justify-content:center}

/* inside */
.photo-band{position:absolute;left:0;top:0;width:1125px;height:190px;display:flex}
.photo-band div{flex:1}
.pic-valley{background:linear-gradient(180deg,#8fc0e8,#b9d79a 45%,#4f8a33)}
.pic-solar{background:linear-gradient(160deg,#6fa8dc,#2d5f9a 50%,#9bb5cc)}
.pic-people{background:linear-gradient(180deg,#f4f6f2,#a9cf73 55%,#5f8f3a)}
.band-curve{position:absolute;left:0;top:110px}
.inside .panel{padding-top:212px}
.inside .services-panel{padding-top:200px}
.inside .h-left{margin-top:18px}
.inside-brand{position:absolute;left:0;bottom:16px;width:230px;height:58px;background:var(--paper);border:3px solid var(--blue);border-left:none;border-radius:0 22px 22px 0;padding-left:26px;font-size:21px}
.inside-brand .dot{width:22px;height:22px}
.bottom-rule{position:absolute;left:0;right:0;bottom:0;height:6px;background:var(--blue)}

.services{list-style:none}
.service{display:flex;gap:16px;margin-bottom:14px}
.service .icon{width:40px;height:40px;background:var(--green);flex:none;display:flex;align-items:center;justify-content:center}
.service h3{color:var(--blue);font-size:13px;font-weight:600;margin-bottom:2px}
.service ul{list-style:none}
.service li{font-size:10.5px;line-height:1.4;padding-left:13px;position:relative}
.service li::before{content:"✓";color:var(--green-dark);position:absolute;left:0;font-weight:700}
.services-panel.right{padding-top:60px}
</style>
</head>
<body>

<!-- Front cover panel -->
<div class="cover-view">
  <section class="panel cover">
    <div class="brand"><span class="dot"></span>BrightLeaf Energy</div>
    <div class="nature-band"><span class="small">Take care of</span><span class="big">Nature</span></div>
    <div class="photo man-photo" role="img" aria-label="Smiling businessman in a suit holding a light bulb and cash"></div>
    <div class="web-bar">www.BrightLeafEnergy.com</div>
  </section>
</div>

<!-- Outside spread -->
<div class="spread outside">
  <section class="panel">
    <div class="section">
      <h2>About Us</h2>
      <p>BrightLeaf Energy is a local company in Fresno, CA with over 25 years of experience in all aspects of construction. We are the only business that specializes in total home and business energy conservation. We offer detailed financial analysis of all considered improvements to ensure you make the best decision possible. We pride ourselves in providing exceptional service, quality products, and competitive pricing. These core values set us apart from other providers in our industry, and we look forward to working with you.</p>
    </div>
    <div class="section">
      <h2>Who We Are</h2>
      <p>BrightLeaf Energy is your all-in-one energy conservation improvement contractor. We help homeowners, business owners, and the private sector reduce energy costs while reducing their carbon footprint.</p>
    </div>
    <div class="photo team-photo" role="img" aria-label="Group of smiling women holding an energy-efficient product"></div>
  </section>

  <section class="panel">
    <h2>Fiscal Responsibility</h2>
    <p>Although solar energy is a green technology with many environmental benefits, at BrightLeaf Energy we understand that your solar energy system must make financial sense as well. That is why we customize your solar energy system utilizing the best components at the best possible prices. We provide you with financial documents including ROI, RRR, IRR cash flow analysis and many other financial models to aid your company in making an educated and informed decision. We believe that fiscal responsibility should be a key component in all decision making.</p>
    <div class="brand mid-brand"><span class="dot"></span>BrightLeaf Energy</div>
    <h2>Contact Us</h2>
    <div class="contact">
      <div class="group">
        <svg class="icon" width="16" height="22" viewBox="0 0 16 22"><path d="M8 0a8 8 0 0 0-8 8c0 6 8 14 8 14s8-8 8-14a8 8 0 0 0-8-8z" fill="var(--blue)"/><circle cx="8" cy="8" r="3" fill="#fff"/></svg>
        4120 Meadowlark Ave Suite 210<br>Fresno, CA 93722
      </div>
      <div class="group">
        <svg class="icon" width="20" height="20" viewBox="0 0 20 20"><path d="M4 1l4 4-2 3c1 3 3 5 6 6l3-2 4 4-3 3C8 18 2 12 1 4z" fill="var(--blue)"/></svg>
        555-204-0411<br>555-318-0982
      </div>
      <div class="group">
        <svg class="icon" width="22" height="16" viewBox="0 0 22 16"><rect width="22" height="16" rx="2" fill="var(--blue)"/><path d="M1 2l10 7 10-7" stroke="#fff" stroke-width="1.6" fill="none"/></svg>
        info@BrightLeafEnergy.com<br>www.BrightLeafEnergy.com
      </div>
    </div>
  </section>

  <section class="panel cover">
    <div class="brand"><span class="dot"></span>BrightLeaf Energy</div>
    <div class="nature-band"><span class="small">Take care of</span><span class="big">Nature</span></div>
    <div class="photo man-photo" role="img" aria-label="Smiling businessman in a suit holding a light bulb and cash"></div>
    <div class="web-bar">www.BrightLeafEnergy.com</div>
  </section>
</div>

<!-- Inside spread -->
<div class="spread inside">
  <div class="photo-band">
    <div class="pic-valley" role="img" aria-label="Green alpine valley with village houses"></div>
    <div class="pic-solar" role="img" aria-label="Woman holding a light bulb beside solar panels"></div>
    <div class="pic-people" role="img" aria-label="Business people with green energy icons"></div>
  </div>
  <svg class="band-curve" width="1125" height="110" viewBox="0 0 1125 110" aria-hidden="true">
    <path d="M0 55 C120 95 240 95 375 60 C470 20 560 10 650 25 C760 45 860 80 1125 40 L1125 110 L0 110 Z" fill="var(--paper)"/>
    <path d="M0 55 C120 95 240 95 375 60 C470 20 560 10 650 25 C760 45 860 80 1125 40" fill="none" stroke="var(--blue)" stroke-width="4"/>
  </svg>

  <section class="panel">
    <h2 class="h-left">What We Offer</h2>
    <p>BrightLeaf Energy offers the best available energy efficient products on the market with competitive pricing. Our multiple licenses and insurance policies allow us to provide competitive pricing options to our customers by packaging several energy efficient products together.</p>
    <h2 style="margin-top:34px">With Our Help</h2>
    <p>BrightLeaf Energy will provide our customers comfort all year round by reducing energy usage and utility bills; saving you money. Making such improvements increases the value of your home and adds even greater curb appeal. We provide multiple financing options and discuss each of those with our customers to provide the best service possible. We also provide 100% financing meaning no money out of pocket from you.</p>
    <div class="brand inside-brand"><span class="dot"></span>BrightLeaf Energy</div>
  </section>

  <section class="panel services-panel">
    <h2>Our Services</h2>
    <ul class="services">
      <li class="service"><span class="icon"><svg width="24" height="24" viewBox="0 0 24 24"><rect x="2" y="4" width="20" height="16" fill="none" stroke="#fff" stroke-width="2"/><path d="M2 12h20M9 4v16M15 4v16" stroke="#fff" stroke-width="1.5"/></svg></span>
        <div><h3>Solar Panels</h3><ul><li>Panels</li><li>Inverters</li></ul></div></li>
      <li class="service"><span class="icon"><svg width="24" height="24" viewBox="0 0 24 24"><circle cx="12" cy="12" r="2.5" fill="#fff"/><path d="M12 10C10 3 15 2 15 6zM14 12c7-2 8 3 4 3zM12 14c2 7-3 8-3 4zM10 12c-7 2-8-3-4-3z" fill="#fff"/></svg></span>
        <div><h3>Heating &amp; AC</h3><ul><li>Allergy Filtration system</li><li>Heat pumps</li><li>Air conditioning</li><li>Duct replacement/sealing</li><li>Whole House Fan</li></ul></div></li>
      <li class="service"><span class="icon"><svg width="24" height="24" viewBox="0 0 24 24"><rect x="4" y="3" width="16" height="18" fill="none" stroke="#fff" stroke-width="2"/><path d="M12 3v18M4 12h16" stroke="#fff" stroke-width="2"/></svg></span>
        <div><h3>Windows &amp; Doors</h3><ul><li>Dual pane windows</li><li>Sealing</li><li>Skylights</li><li>Doors</li></ul></div></li>
      <li class="service"><span class="icon"><svg width="24" height="24" viewBox="0 0 24 24"><circle cx="12" cy="10" r="6" fill="none" stroke="#fff" stroke-width="2"/><rect x="9" y="17" width="6" height="4" fill="#fff"/></svg></span>
        <div><h3>Lighting</h3><ul><li>LED</li><li>Lighting controls</li><li>Lighting fixtures</li></ul></div></li>
      <li class="service"><span class="icon"><svg width="24" height="24" viewBox="0 0 24 24"><path d="M2 13L12 4l10 9" fill="none" stroke="#fff" stroke-width="2.5"/><path d="M6 12v8h12v-8" fill="none" stroke="#fff" stroke-width="2"/></svg></span>
        <div><h3>Roofing</h3><ul><li>Roof replacement</li><li>Awnings</li><li>Window treatments</li><li>Radiant Barrier</li></ul></div></li>
    </ul>
  </section>

  <section class="panel services-panel right" style="padding-top:200px">
    <ul class="services">
      <li class="service"><span class="icon"><svg width="24" height="24" viewBox="0 0 24 24"><path d="M3 12L12 4l9 8v8H3z" fill="none" stroke="#fff" stroke-width="2"/><path d="M6 16h12M6 19h12" stroke="#fff" stroke-width="1.5"/></svg></span>
        <div><h3>Insulation</h3><ul><li>Attics</li><li>Attic fan</li><li>Walls</li><li>Under-floor</li></ul></div></li>
      <li class="service"><span class="icon"><svg width="24" height="24" viewBox="0 0 24 24"><path d="M4 6h12v4H4zM14 10v3" stroke="#fff" stroke-width="2" fill="none"/><path d="M14 15c-2 3 0 6 0 6s2-3 0-6z" fill="#fff"/></svg></span>
        <div><h3>Water Saving</h3><ul><li>Low flow plumbing, fixtures, toilets, shower heads</li></ul></div></li>
      <li class="service"><span class="icon"><svg width="24" height="24" viewBox="0 0 24 24"><path d="M4 21c0-8 2-12 4-14M10 21c0-9 2-13 4-16M16 21c0-7 2-10 4-12" stroke="#fff" stroke-width="2" fill="none"/></svg></span>
        <div><h3>Landscaping</h3><ul><li>Drip irrigation</li><li>Rainwater catchment systems</li><li>Artificial turf</li><li>Drought Tolerant Landscaping</li></ul></div></li>
      <li class="service"><span class="icon"><svg width="24" height="24" viewBox="0 0 24 24"><path d="M14 2L5 14h6l-2 8 9-12h-6z" fill="#fff"/></svg></span>
        <div><h3>Energy Audit</h3><ul><li>Certified detailed analysis of prioritized energy saving recommendations</li></ul></div></li>
      <li class="service"><span class="icon"><svg width="24" height="24" viewBox="0 0 24 24"><rect x="7" y="3" width="10" height="18" rx="2" fill="none" stroke="#fff" stroke-width="2"/><path d="M13 6l-3 6h3l-2 5" stroke="#fff" stroke-width="1.8" fill="none"/></svg></span>
        <div><h3>Electric</h3><ul><li>Vehicle Charging Station</li><li>Pool Pumps</li><li>Electric or Natural Heat Pump Pool Heater</li><li>Electric or Natural Gas Water Heater</li><li>Electric or Natural Gas Tankless Water Heater</li></ul></div></li>
    </ul>
  </section>
  <div class="bottom-rule"></div>
</div>

</body>
</html>
```